Postcard needed for expert witness service

Looking for a professional postcard that will be mailed to personal injury lawyers / law firms to introduce my expert witness services.

Target Market(s)

Law firms, personal injury lawyers

Industry/Entity Type

Expert witness, law

Font styles to use
Sans Serif

Requirements
Must have
• Logo: The Frost Counsel [Main Heading]Do you handle snow and ice related slip and falls? Darrel is one of the top snow industry experts in the country! [Following should be in a list type fashion, possibly bulleted]Darrel's credentials: Accredited Winter Practitioner (AWP), past WRTA board member and chair, former ISO 9001 certified snow company owner , 32 years in the industry. (555) 284-3917 NOTES: Postcard will be 4" x 6" Please use both sides however must have room for labels and stamp
Should not have
• Wouldn't suggest using both photos on same side. Honestly, feel free to only use one of the slip and fall photos if it works out better. Thanks!

```html
<!DOCTYPE html>
<html lang="en">
<head>
<meta charset="UTF-8">
<title>The Frost Counsel – Postcard</title>
<link href="https://fonts.googleapis.com/css2?family=Montserrat:wght@400;600;700&family=Raleway:wght@300;400&display=swap" rel="stylesheet">
<style>
  :root {
    --page: #e9e9e9;
    --panel-dark: #231f20;
    --white: #ffffff;
    --ink: #1e1e1e;
    --photo-ice: #b9c0c6;
    --photo-denim: #5a6f8c;
    --photo-coat: #5b4a44;
  }
  * { box-sizing: border-box; margin: 0; padding: 0; }
  html, body { width: 1075px; height: 1200px; overflow: hidden; }
  body { background: var(--page); position: relative; font-family: "Montserrat", sans-serif; }

  .postcard { position: absolute; left: 144px; width: 786px; height: 523px; overflow: hidden; background: var(--white); }
  .postcard--front { top: 66px; }
  .postcard--back { top: 628px; }

  .front-photo {
    position: absolute; inset: 0;
    background: linear-gradient(160deg, #8c8f93 0%, var(--photo-denim) 35%, var(--photo-ice) 70%, #dfe1e2 100%);
  }
  .front-panel { position: absolute; inset: 0; width: 100%; height: 100%; }

  .wordmark {
    position: absolute; font-family: "Montserrat", sans-serif; font-weight: 600;
    font-size: 34px; line-height: 1; white-space: nowrap;
  }
  .postcard--front .wordmark { right: 60px; top: 80px; color: var(--white); }
  .postcard--back .wordmark { left: 46px; top: 60px; color: var(--ink); font-size: 30px; }

  .headline {
    position: absolute; right: 60px; top: 168px; width: 380px;
    color: var(--white); font-weight: 700; font-size: 27px; line-height: 36px; text-align: right;
  }
  .tagline {
    position: absolute; right: 60px; top: 302px; width: 340px;
    color: var(--white); font-family: "Raleway", sans-serif; font-weight: 400; font-size: 21px; line-height: 26px; text-align: right;
  }
  .phone-band {
    position: absolute; left: 399px; right: 0; top: 419px; height: 54px; background: var(--white);
    display: flex; align-items: center; padding-left: 31px;
  }
  .phone { font-weight: 700; font-size: 37px; letter-spacing: 0.5px; color: var(--ink); line-height: 1; }

  .credentials { position: absolute; font-size: 12px; line-height: 1.4; font-weight: 400; }
  .postcard--front .credentials { left: 50px; top: 422px; width: 320px; color: var(--ink); }

  .back-photo {
    position: absolute; left: 0; top: 0; width: 560px; height: 100%;
    background: linear-gradient(90deg, rgba(90,74,68,0.9) 0%, rgba(120,108,104,0.85) 45%, rgba(216,216,214,0.6) 78%, rgba(255,255,255,0) 100%),
                linear-gradient(180deg, #a9a6a3 0%, var(--photo-coat) 55%, #6e6a68 100%);
    -webkit-mask-image: linear-gradient(90deg, #000 70%, transparent 100%);
    mask-image: linear-gradient(90deg, #000 70%, transparent 100%);
  }
  .postcard--back .phone { position: absolute; left: 48px; top: 346px; color: var(--white); }
  .postcard--back .credentials { left: 48px; top: 410px; width: 360px; color: var(--white); font-size: 13px; }

  .stamp-box { position: absolute; left: 586px; top: 44px; width: 146px; height: 160px; border: 2px solid var(--ink); }
  .address-line { position: absolute; left: 499px; width: 233px; height: 0; border-top: 1.5px solid var(--ink); }
</style>
</head>
<body>

<section class="postcard postcard--front">
  <div class="front-photo" role="img" aria-label="Photo of a person slipping and falling on an icy sidewalk"></div>
  <svg class="front-panel" viewBox="0 0 786 523" preserveAspectRatio="none" aria-hidden="true">
    <polygon points="242,0 786,0 786,523 500,523" fill="var(--panel-dark)"/>
  </svg>
  <div class="wordmark">The Frost Counsel</div>
  <h1 class="headline">Do you handle snow<br>and ice related slip<br>and falls?</h1>
  <p class="tagline">Darrel is one of the top<br>snow industry experts<br>in the country!</p>
  <div class="phone-band"><span class="phone">(555) 284-3917</span></div>
  <p class="credentials">Darrel's credentials: Accredited Winter Practitioner (AWP), past WRTA board member and chair, former ISO 9001 certified snow company owner , 32 years in the industry.</p>
</section>

<section class="postcard postcard--back">
  <div class="back-photo" role="img" aria-label="Photo of a woman in a winter coat and knit hat who has fallen on snowy ground"></div>
  <div class="wordmark">The Frost Counsel</div>
  <span class="phone">(555) 284-3917</span>
  <p class="credentials">Darrel's credentials: Accredited Winter Practitioner (AWP), past WRTA board member and chair, former ISO 9001 certified snow company owner , 32 years in the industry.</p>
  <div class="stamp-box"></div>
  <div class="address-line" style="top:334px"></div>
  <div class="address-line" style="top:374px"></div>
  <div class="address-line" style="top:415px"></div>
</section>

</body>
</html>
```